For a German comparison website comparing the best online trading brokers I need 10 banners for Facebook advertising. The banners should be a size of 1200x628 with one of the following texts:
1) Traden für Anfänger
25 Euro gratis
2) Traden Sie online
25 Euro gratis
3) Online-Trading für Anfänger
4) Trading für Einsteiger
25 Euro gratis
5) Aktien für Einsteiger
25 Euro gratis
The targeted website is www.marvolink.ch and it compares brokers where traders can trade shares, commodities,indices and Forex.

```html
<!DOCTYPE html>
<html lang="de">
<head>
<meta charset="utf-8">
<title>Traden für Anfänger – Bannerserie</title>
<link href="https://fonts.googleapis.com/css2?family=Roboto+Condensed:wght@400;700&family=Roboto:wght@400;500&family=Ubuntu:wght@500&family=Libre+Baskerville&display=swap" rel="stylesheet">
<style>
:root{
  --green:#a3b852;
  --green-text:#b5c95a;
  --green-light:#c4d37e;
  --green-deep:#3d4a22;
  --seal:#8a9e3e;
  --dark:#333333;
  --ink:#111111;
  --white:#ffffff;
}
*{margin:0;padding:0;box-sizing:border-box}
html,body{width:1200px;height:1200px;overflow:hidden;background:var(--white)}
body{position:relative;font-family:"Roboto Condensed",sans-serif}
.label{position:absolute;font-family:"Roboto Condensed",sans-serif;font-weight:700;font-size:52px;color:var(--ink);line-height:1}
.banner{position:absolute;width:427px;height:223px;overflow:hidden}
.col-a{left:110px}.col-b{left:743px;width:426px}
.row-1{top:10px}.row-2{top:245px}.row-3{top:486px}.row-4{top:722px}.row-5{top:966px}
.photo{position:absolute;inset:0}
.abs{position:absolute}
.center{left:0;right:0;text-align:center}
.caps{text-transform:uppercase}

/* 1 */
.b1 .photo{background:radial-gradient(ellipse at 55% 20%,#3c5152,#22302f 60%,#18211f)}
.b1 .sub{top:88px;font-size:14px;color:var(--green-text)}
.b1 .head{top:108px;font-size:27px;font-weight:700;color:var(--green-text)}

/* 2 */
.b2 .photo{left:133px;background:linear-gradient(135deg,#5b4a52 0%,#b7b4b6 35%,#9a8c82 70%,#6d5038 100%)}
.b2 .panel{left:0;top:0;width:133px;height:223px;background:var(--green);color:var(--white);padding:60px 0 0 14px;line-height:1.25}
.b2 .sub{font-size:15px}
.b2 .num{font-size:23px;font-weight:700;margin-top:5px}
.b2 .head{font-size:15px;font-weight:700}

/* 3 */
.b3 .photo{background:linear-gradient(120deg,#c9bfae,#e6ddcc 45%,#d6cab6 80%,#b8a995)}
.b3 .panel{left:228px;top:0;width:132px;height:223px;background:var(--dark);text-align:center;font-family:"Ubuntu",sans-serif;color:var(--green-text)}
.b3 .rule{position:absolute;left:14px;right:14px;height:3px;background:#3e3e3e}
.b3 .sub{position:absolute;left:0;right:0;top:60px;font-size:9px;font-family:"Roboto",sans-serif}
.b3 .num{position:absolute;left:0;right:0;top:72px;font-size:38px;line-height:1}
.b3 .head{position:absolute;left:0;right:0;top:113px;font-size:17px;line-height:1.2}

/* 4 */
.b4 .photo{background:linear-gradient(180deg,#e8a98a 0%,#f1b685 35%,#c99c8a 60%,#9d95a0 80%,#b7aeb2 100%)}
.b4 .sub{top:39px;font-size:11px;color:#222;display:flex;justify-content:center;align-items:center;gap:6px}
.b4 .sub i{display:block;width:24px;height:1px;background:#333}
.b4 .head{top:56px;font-size:25px;font-weight:700;color:#1a1a1a}

/* 5 */
.b5 .photo{background:radial-gradient(ellipse at 70% 55%,#2f7a1c,#123d0c 45%,#040a03 85%)}
.b5 .seal{left:34px;top:14px;width:100px;height:100px;border-radius:50%;background:var(--seal);color:#2a2a1a;text-align:center;font-weight:700;line-height:1}
.b5 .seal .sub{position:absolute;left:0;right:0;top:20px;font-size:7.5px;letter-spacing:.6px}
.b5 .seal .mid{position:absolute;left:0;right:0;top:32px;font-size:17px}
.b5 .seal .head{position:absolute;left:0;right:0;top:50px;font-size:26px}

/* 6 */
.b6 .photo{background:linear-gradient(180deg,#0f1a45 0%,#1c2a5a 45%,#4a4330 75%,#2a241a 100%)}
.b6 .box{left:101px;top:58px;width:224px;height:106px;background:rgba(220,220,225,.85);text-align:center}
.b6 .sub{position:absolute;left:0;right:0;top:32px;font-size:9px;color:#222}
.b6 .head{position:absolute;left:0;right:0;top:45px;font-size:25px;font-weight:700;color:#111;display:flex;justify-content:center;align-items:center;gap:2px}

/* 7 */
.b7{background:var(--green)}
.b7 .txt{left:157px;top:80px;font-family:"Libre Baskerville",serif;color:var(--green-deep);line-height:1}
.b7 .sub{font-size:7.5px;letter-spacing:.3px}
.b7 .head{font-size:23px;letter-spacing:1px;margin-top:3px;line-height:1}

/* 8 */
.b8{background:var(--green)}
.b8 .art{left:10px;top:14px;width:190px;height:170px;background:linear-gradient(135deg,#95a94a,#8a9c44)}
.b8 .txt{left:241px;top:94px;color:var(--white);font-family:"Roboto",sans-serif}
.b8 .sub{font-size:11.5px}
.b8 .head{font-size:16px;margin-top:3px}

/* 9 */
.b9 .photo{background:radial-gradient(ellipse at 50% 30%,#5a5246,#262420 45%,#0c0c0c 80%)}
.b9 .band{left:110px;top:66px;width:203px;height:78px;background:rgba(20,20,20,.7)}
.b9 .sub{left:110px;width:203px;top:94px;text-align:center;font-size:10.5px;color:var(--green-text);font-family:"Roboto",sans-serif}
.b9 .head{left:110px;width:203px;top:107px;text-align:center;font-size:17px;font-weight:700;color:var(--white)}

/* 10 */
.b10{background:var(--dark)}
.b10 .txt{right:249px;top:94px;text-align:right;font-family:"Roboto",sans-serif}
.b10 .sub{font-size:10px;color:var(--green-text)}
.b10 .head{font-size:16px;font-weight:500;color:var(--white);margin-top:3px}
.b10 .divider{left:183px;top:92px;width:1px;height:40px;background:#4a4a4a}
.b10 .art{left:271px;top:57px;width:126px;height:101px;background:#262626}
</style>
</head>
<body>

<div class="label" style="left:60px;top:132px">1</div>
<div class="label" style="left:60px;top:327px">2</div>
<div class="label" style="left:60px;top:583px">3</div>
<div class="label" style="left:60px;top:805px">4</div>
<div class="label" style="left:60px;top:1048px">5</div>
<div class="label" style="left:692px;top:116px">6</div>
<div class="label" style="left:692px;top:350px">7</div>
<div class="label" style="left:692px;top:586px">8</div>
<div class="label" style="left:692px;top:826px">9</div>
<div class="label" style="left:668px;top:1050px">10</div>

<!-- 1 -->
<section class="banner col-a row-1 b1">
  <div class="photo" role="img" aria-label="Dunkles Foto: Person hinter Börsenkursen mit steigender Kurslinie"></div>
  <p class="abs center sub caps">Traden für Anfänger</p>
  <p class="abs center head caps">25 Euro Gratis</p>
</section>

<!-- 2 -->
<section class="banner col-a row-2 b2">
  <div class="photo" role="img" aria-label="Foto: Hände halten Smartphone mit Kursliste über einer Laptop-Tastatur"></div>
  <div class="abs panel">
    <p class="sub caps">Traden für<br>Anfänger</p>
    <p class="num">25</p>
    <p class="head caps">Euro Gratis</p>
  </div>
</section>

<!-- 3 -->
<section class="banner col-a row-3 b3">
  <div class="photo" role="img" aria-label="Foto: Finanzteil einer Zeitung mit Kurstabellen"></div>
  <div class="abs panel">
    <div class="rule" style="top:50px"></div>
    <p class="sub caps">Traden für Anfänger</p>
    <p class="num">25</p>
    <p class="head caps">Euro<br>Gratis</p>
    <div class="rule" style="top:155px"></div>
  </div>
</section>

<!-- 4 -->
<section class="banner col-a row-4 b4">
  <div class="photo" role="img" aria-label="Foto: Stadtpanorama mit Dom und Brücke im Sonnenuntergang"></div>
  <svg class="abs" style="left:200px;top:17px" width="26" height="20" viewBox="0 0 26 20">
    <polyline points="2,18 8,10 13,13 22,3" fill="none" stroke="#222" stroke-width="1.6"/>
  </svg>
  <p class="abs center sub caps"><i></i>Traden für Anfänger<i></i></p>
  <p class="abs center head caps">25 Euro Gratis</p>
</section>

<!-- 5 -->
<section class="banner col-a row-5 b5">
  <div class="photo" role="img" aria-label="Foto: grün leuchtende Börsenbildschirme mit Balkendiagrammen"></div>
  <div class="abs seal">
    <p class="sub caps">Traden für Anfänger</p>
    <p class="mid caps">25 Euro</p>
    <p class="head caps">Gratis</p>
  </div>
</section>

<!-- 6 -->
<section class="banner col-b row-1 b6">
  <div class="photo" role="img" aria-label="Foto: nächtliches Stadtzentrum mit beleuchtetem Rathaus und Weihnachtsbaum"></div>
  <div class="abs box">
    <p class="sub caps">Traden für Anfänger</p>
    <p class="head caps">25 Euro Gratis
      <svg width="22" height="20" viewBox="0 0 22 20"><path d="M1,2 V19 H21" fill="none" stroke="#111" stroke-width="2"/><path d="M4,17 V10 L8,14 L12,6 L15,11 L19,4 V17 Z" fill="#111"/></svg>
    </p>
  </div>
</section>

<!-- 7 -->
<section class="banner col-b row-2 b7">
  <div class="abs txt">
    <p class="sub caps">Traden für Anfänger</p>
    <p class="head caps">25 Euro<br>Gratis</p>
  </div>
  <svg class="abs" style="left:0;top:0" width="426" height="223">
    <polyline points="249,166 281,127 313,163 345,123" fill="none" stroke="var(--green-light)" stroke-width="2.5"/>
    <g fill="var(--green)" stroke="var(--green-light)" stroke-width="2.5">
      <circle cx="249" cy="166" r="6"/><circle cx="281" cy="127" r="6"/>
      <circle cx="313" cy="163" r="6"/><circle cx="345" cy="123" r="6"/>
    </g>
  </svg>
</section>

<!-- 8 -->
<section class="banner col-b row-3 b8">
  <div class="abs art" role="img" aria-label="Illustration: Diagrammachse mit zwei steigenden Pfeilen"></div>
  <div class="abs txt">
    <p class="sub">Traden Für Anfänger</p>
    <p class="head">25 Euro Gratis</p>
  </div>
</section>

<!-- 9 -->
<section class="banner col-b row-4 b9">
  <div class="photo" role="img" aria-label="Foto: beleuchtetes Triumphtor bei Nacht mit Lichtspuren des Verkehrs"></div>
  <div class="abs band"></div>
  <svg class="abs" style="left:262px;top:80px" width="40" height="56" viewBox="0 0 40 56">
    <polyline points="2,52 14,10 26,44 31,32 37,50" fill="none" stroke="#5a5650" stroke-width="5"/>
  </svg>
  <p class="abs sub">Traden Für Anfänger</p>
  <p class="abs head caps">25 Euro Gratis</p>
</section>

<!-- 10 -->
<section class="banner col-b row-5 b10">
  <div class="abs txt">
    <p class="sub">Traden Für Anfänger</p>
    <p class="head caps">25 Euro Gratis</p>
  </div>
  <div class="abs divider"></div>
  <div class="abs art" role="img" aria-label="Illustration: Browserfenster mit steigendem Kursdiagramm"></div>
</section>

</body>
</html>
```